ALL TEXT Social Media Graphics

We are looking for a series of social media graphics for Instagram (new size: 4:5 (1080 x 1350 pixels) ratio that are ALL TEXT. We want the following quotes below on each graphic; one quote per graphic. AND, In very small letters at the bottom of each graphic, add @PaulaWrenLive
The look and feel of these graphics should be complimentary to the color palette attached below; but keep them simple. But the design is up to you; at the end of this document, I provided various samples of all text graphics that I like as examples.
The Quotes are in the attached WORD document
women trying to lose weight

```html
<!DOCTYPE html>
<html lang="en">
<head>
<meta charset="UTF-8">
<title>Glow Girl Summer Reset</title>
<link href="https://fonts.googleapis.com/css2?family=Montserrat:wght@400;700&display=swap" rel="stylesheet">
<style>
  :root {
    --bg: #ffffff;
    --pink: #ef6496;
    --pink-soft: #f4a3be;
    --ink: #262626;
  }
  * { margin: 0; padding: 0; box-sizing: border-box; }
  html, body {
    width: 960px;
    height: 1200px;
    overflow: hidden;
    background: var(--bg);
  }
  .post {
    position: relative;
    width: 960px;
    height: 1200px;
    background: linear-gradient(to bottom, var(--bg) 0%, var(--bg) 76%, var(--pink-soft) 100%);
    font-family: "Montserrat", sans-serif;
  }
  .headline {
    position: absolute;
    left: 55px;
    top: 78px;
    width: 880px;
    color: var(--pink);
    font-weight: 700;
    font-size: 76px;
    line-height: 105px;
    letter-spacing: -0.5px;
  }
  .call-to-action {
    position: absolute;
    right: 107px;
    top: 684px;
    width: 840px;
    text-align: right;
    color: var(--ink);
    font-weight: 700;
    font-size: 71px;
    line-height: 105px;
    letter-spacing: 0.3px;
  }
  .handle {
    position: absolute;
    left: 0;
    right: 0;
    top: 1092px;
    text-align center;
    text-align: center;
    color: var(--ink);
    font-weight: 400;
    font-size: 29px;
    letter-spacing: 0.5px;
  }
</style>
</head>
<body>
  <main class="post">
    <h1 class="headline">If your goal is a tiny<br>waist, flat belly, and<br>30 pounds<br>down—this is the<br>plan.</h1>
    <p class="call-to-action">Comment “Summer”<br>to join the Glow Girl<br>Summer Reset!</p>
    <p class="handle">@PaulaWrenLive</p>
  </main>
</body>
</html>
```